Vessel Relay - Corporate Stationery (Medical Start Up)
Business Card | Name Tag | Letter Head | Email Signature
Vessel Relay - Corporate Stationery (Medical Start Up) - Medical
Creative Brief
Use specific fonts
Times New Roman and Roboto Regular
Professional
Martin Keogh
CEO
PO BOX R482 Sydney NSW 2000 AUSTRALIA
Martin@vesselrelay.example
www.vesselrelay.example
Powered by Lunar Heron (ABN 98 765 432 101)
(1) Please use the uploaded corporate logo (2) Entries should include one draft that includes the colours of the uploaded logo (3) In addition, Designers are encouraged to present the same logo in different colours (4) The use of a water mark or shadow as a design concept is encouraged (5) Designs need to include example of how the logo will look across the following applications: Business Card | Name Tag | Letter Head | Email Signature (6) The words "Chain of Custody" can be included outside the logo should this be considered desirable by the designer (7) Likewise, elements such as "Vessel Relay", the "shield logo" or concepts there of can be used at the designers discretion (8) Powered by Lunar Heron (ABN 98 765 432 101) needs to be included (9) Use of both sides of the business card is mandatory (10) Please note it's not "Cell", but "Mobile" or "M" or "m" (11) Please use the designated fonts contained in the uploaded file
Design elements on the front and back of the business card are at the designers discretion. A double sided Business Card is preferred.
Dorian Dorian
Dear Designers, Thank you for the innovative designs. A new set of master AI files have been uploaded. Please note that there are different colour versions. Could you please present the stationery in those colours versions plus another other combinations you feel might look good. A separate supplementary design brief has also been uploaded for your assistance. Please read this supplementary design brief. Questions are always welcome.

```html
<!DOCTYPE html>
<html lang="en">
<head>
<meta charset="utf-8">
<title>Vessel Relay – Corporate Stationery</title>
<link rel="stylesheet" href="https://fonts.googleapis.com/css2?family=Roboto:wght@400;700&family=Tinos:ital,wght@0,400;1,700&display=swap">
<style>
:root{
  --stage:#b4b4b4;
  --paper:#ffffff;
  --ink:#1a1a1a;
  --muted:#7a7a7a;
  --line:#c9c9c9;
  --yellow:#f8c51c;
  --amber:#f5a413;
  --orange:#ef8a12;
  --black:#111111;
}
*{box-sizing:border-box;margin:0;padding:0}
html,body{width:1200px;height:754px;overflow:hidden;background:var(--stage)}
body{position:relative;font-family:"Roboto",Arial,sans-serif;color:var(--ink)}
.sheet{position:absolute;background:var(--paper);overflow:hidden;box-shadow:0 1px 3px rgba(0,0,0,.25)}

.brand{position:absolute;display:flex;align-items:center;gap:5px;font-family:"Roboto",Arial,sans-serif;font-weight:700;color:var(--ink);white-space:nowrap}
.brand-mark{display:block;background:var(--yellow)}
.brand.on-dark{color:#fff}

.contact{position:absolute;font-size:6px;line-height:9px;color:var(--muted);white-space:nowrap}
.contact li{list-style:none;display:flex;align-items:center;gap:4px}
.contact li::before{content:"";width:4px;height:4px;background:var(--amber);display:block}

.band{position:absolute;left:0;right:0;display:flex;height:26px}
.band-address{background:linear-gradient(90deg,var(--yellow),var(--amber));color:var(--ink);font-size:6.5px;line-height:8px;padding:5px 10px;font-weight:700}
.band-abn{flex:1;display:flex;align-items:center;padding-left:10px;font-size:7px;font-weight:700;border-top:1px solid var(--line)}
.band-end{background:var(--black);display:flex;align-items:center;justify-content:center}
.band-end span{width:11px;height:11px;background:var(--yellow)}

.letter-body{position:absolute;left:30px;right:40px;top:104px;font-size:6px;line-height:9px;color:var(--muted)}
.letter-body p{margin-bottom:8px}
.signature{display:block;width:60px;height:14px;background:linear-gradient(90deg,#d8d8d8,#eeeeee);margin:10px 0 4px}

.name-bar{position:absolute;background:linear-gradient(90deg,var(--yellow),var(--orange));font-size:7px;font-weight:700;padding:3px 8px;line-height:9px}
.name-bar small{display:block;font-weight:400;font-size:6px}

.compliment-title{position:absolute;font-family:"Tinos","Times New Roman",serif;font-style:italic;font-weight:700;font-size:15px;color:var(--ink)}

.folder-panel{position:absolute;top:0;bottom:0;width:50%;overflow:hidden}
.mini-lines i{display:block;height:2px;background:#d6d6d6;margin-bottom:3px}
</style>
</head>
<body>

<!-- Long slip -->
<section class="sheet slip-long" style="left:34px;top:34px;width:394px;height:139px">
  <div class="brand" style="left:14px;top:14px;font-size:13px"><span class="brand-mark" style="width:13px;height:13px"></span>Vessel Relay</div>
  <ul class="contact" style="left:290px;top:12px">
    <li>+61 2 5550 0134</li><li>+61 4 5550 0178</li><li>Martin@vesselrelay.example</li><li>www.vesselrelay.example</li>
  </ul>
  <div class="band" style="top:98px;height:29px">
    <div class="band-address" style="width:220px">PO BOX R482<br>Sydney NSW 2000 AUSTRALIA</div>
    <div class="band-abn">ABN 98 765 432 101</div>
    <div class="band-end" style="width:70px"><span></span></div>
  </div>
</section>

<!-- Letterhead -->
<section class="sheet letterhead" style="left:34px;top:187px;width:394px;height:526px">
  <div class="brand" style="left:30px;top:24px;font-size:14px"><span class="brand-mark" style="width:14px;height:14px"></span>Vessel Relay</div>
  <ul class="contact" style="left:290px;top:20px">
    <li>+61 2 5550 0134</li><li>+61 4 5550 0178</li><li>Martin@vesselrelay.example</li><li>www.vesselrelay.example</li>
  </ul>
  <div class="contact" style="left:310px;top:80px">7 May 2024</div>
  <div class="letter-body">
    <p>Mr Alan Hart<br>Suite 4, 20 Harbour St<br>Sydney NSW 2000</p>
    <p>Dear Alan,</p>
    <p>Thank you for meeting with our team last week. We were pleased to discuss how our chain of custody service can support your clinics and laboratories across the state.</p>
    <p>Our platform records every handover of a sample from collection to result, giving staff a clear and secure record at each step of the journey.</p>
    <p>Please find our proposal enclosed. We look forward to hearing from you.</p>
    <p>Yours sincerely,<span class="signature" role="img" aria-label="Handwritten signature"></span>Martin Keogh<br>CEO</p>
  </div>
  <div class="band" style="top:490px;height:28px">
    <div class="band-address" style="width:220px">PO BOX R482<br>Sydney NSW 2000 AUSTRALIA</div>
    <div class="band-abn">ABN 98 765 432 101</div>
    <div class="band-end" style="width:70px"><span></span></div>
  </div>
</section>

<!-- Business card front -->
<section class="sheet card-front" style="left:502px;top:34px;width:233px;height:115px">
  <div class="brand" style="left:12px;top:12px;font-size:11px"><span class="brand-mark" style="width:11px;height:11px"></span>Vessel Relay</div>
  <div class="name-bar" style="left:120px;right:0;top:32px">Martin Keogh<small>CEO</small></div>
  <ul class="contact" style="left:124px;top:58px;font-size:5.5px;line-height:8px">
    <li>+61 2 5550 0134</li><li>+61 4 5550 0178</li><li>Martin@vesselrelay.example</li><li>www.vesselrelay.example</li>
  </ul>
  <div class="contact" style="left:12px;top:78px;font-size:5.5px;line-height:8px">PO BOX R482<br>Sydney NSW 2000<br>AUSTRALIA</div>
  <div style="position:absolute;left:0;right:0;bottom:0;height:6px;background:linear-gradient(90deg,var(--yellow),var(--orange))"></div>
</section>

<!-- Business card back -->
<section class="sheet card-back" style="left:502px;top:163px;width:233px;height:120px;background:var(--black)">
  <div class="brand on-dark" style="left:50%;top:50%;transform:translate(-50%,-50%);font-size:15px"><span class="brand-mark" style="width:15px;height:15px"></span>Vessel Relay</div>
</section>

<!-- With compliments slip -->
<section class="sheet compliment" style="left:451px;top:353px;width:286px;height:161px">
  <div class="brand" style="left:12px;top:14px;font-size:11px"><span class="brand-mark" style="width:11px;height:11px"></span>Vessel Relay</div>
  <div class="compliment-title" style="left:160px;top:14px">With Compliment</div>
  <ul class="contact" style="left:20px;top:60px">
    <li>+61 2 5550 0134</li><li>+61 4 5550 0178</li><li>Martin@vesselrelay.example</li><li>www.vesselrelay.example</li>
  </ul>
  <div class="band" style="top:120px">
    <div class="band-address" style="width:150px;font-size:6px;line-height:7.5px">PO BOX R482<br>Sydney NSW 2000 AUSTRALIA</div>
    <div class="band-abn" style="font-size:6px">ABN 98 765 432 101</div>
    <div class="band-end" style="width:42px"><span></span></div>
  </div>
</section>

<!-- DL slip -->
<section class="sheet slip-dl" style="left:451px;top:538px;width:286px;height:158px">
  <div class="brand" style="left:12px;top:14px;font-size:11px"><span class="brand-mark" style="width:11px;height:11px"></span>Vessel Relay</div>
  <ul class="contact" style="left:178px;top:12px">
    <li>+61 2 5550 0134</li><li>+61 4 5550 0178</li><li>Martin@vesselrelay.example</li><li>www.vesselrelay.example</li>
  </ul>
  <div class="band" style="top:112px">
    <div class="band-address" style="width:150px;font-size:6px;line-height:7.5px">PO BOX R482<br>Sydney NSW 2000 AUSTRALIA</div>
    <div class="band-abn" style="font-size:6px">ABN 98 765 432 101</div>
    <div class="band-end" style="width:42px"><span></span></div>
  </div>
</section>

<!-- Folder cover -->
<section class="sheet folder-cover" style="left:761px;top:34px;width:415px;height:214px">
  <div class="folder-panel" style="left:0;background:linear-gradient(160deg,#ffffff 40%,#fff3d2)">
    <ul class="contact" style="left:16px;bottom:16px;font-size:5px;line-height:7px">
      <li>+61 2 5550 0134</li><li>Martin@vesselrelay.example</li><li>www.vesselrelay.example</li>
    </ul>
  </div>
  <div class="folder-panel" style="left:50%;background:radial-gradient(ellipse at 40% 55%,#fff7d6 0%,var(--yellow) 45%,var(--orange) 100%)">
    <div class="brand" style="left:50%;top:14px;transform:translateX(-50%);font-size:12px"><span class="brand-mark" style="width:12px;height:12px;background:var(--black)"></span>Vessel Relay</div>
  </div>
</section>

<!-- Folder inside -->
<section class="sheet folder-inside" style="left:761px;top:278px;width:415px;height:230px">
  <div class="folder-panel" style="left:0;background:linear-gradient(180deg,#ffffff 55%,#fde7a0 80%,var(--amber))"></div>
  <div class="folder-panel" style="left:50%;background:#fff;border-left:1px solid #e2e2e2">
    <div style="position:absolute;left:22px;right:22px;top:14px;bottom:0;background:#fff;box-shadow:0 0 3px rgba(0,0,0,.2);padding:12px 14px">
      <div class="brand" style="position:static;font-size:7px;gap:3px;margin-bottom:14px"><span class="brand-mark" style="width:7px;height:7px"></span>Vessel Relay</div>
      <div class="mini-lines"><i style="width:90%"></i><i style="width:80%"></i><i style="width:95%"></i><i style="width:70%"></i><i style="width:88%"></i></div>
    </div>
    <svg style="position:absolute;left:0;bottom:0" width="208" height="90" viewBox="0 0 208 90">
      <defs><linearGradient id="pocket" x1="0" y1="0" x2="0" y2="1"><stop offset="0" stop-color="#fff6d0"/><stop offset="1" stop-color="#f5a413"/></linearGradient></defs>
      <path d="M0 30 Q104 -10 208 30 L208 90 L0 90 Z" fill="url(#pocket)"/>
    </svg>
  </div>
</section>

<!-- Envelope -->
<section class="sheet envelope" style="left:828px;top:535px;width:348px;height:161px">
  <svg style="position:absolute;left:0;top:0" width="348" height="70" viewBox="0 0 348 70">
    <defs><linearGradient id="flap" x1="0" y1="0" x2="0" y2="1"><stop offset="0" stop-color="#f8c51c"/><stop offset="1" stop-color="#fff1bf"/></linearGradient></defs>
    <polygon points="0,0 348,0 174,62" fill="url(#flap)"/>
  </svg>
  <span style="position:absolute;left:167px;top:40px;width:14px;height:14px;background:var(--black)"></span>
</section>

</body>
</html>
```